Small butcher shop from Austria needs great powerpoint presentation

We are looking for a powerpoint template for our new CI - it should be modern and clear.

Logo (2 Versions), Slogan, Business Card and Car-Wrap-Design already exist. (See documents below.)

We won't use much text. About 50% of the presentation should be pictures, included in different ways.

We are a family business in Upper Austria, only process animals from farms in the immediate vicinity, produce the products by hand, value animal welfare and short transport routes and avoid packaging as much as possible.

The design should be modern and clear.

Font styles to use
Sans Serif

Requirements
Should not have
• Use the red color sparingly. Only use sans serif fonts (Myriad Pro - if possible). The logo needs to be on first and last page only.

```html
<!DOCTYPE html>
<html lang="de">
<head>
<meta charset="utf-8">
<title>Hofmark – Präsentationsvorlage</title>
<link rel="stylesheet" href="https://fonts.googleapis.com/css2?family=Source+Sans+3:wght@400;600;700&display=swap">
<style>
  :root{
    --page:#7e7e7e;
    --red:#9c1d2f;
    --red-dark:#6f1422;
    --brown:#7b6a5c;
    --brown-dark:#5f5045;
    --ink:#3a3a3a;
    --muted:#8c8c8c;
    --white:#ffffff;
    --meat:linear-gradient(135deg,#c9585a 0%,#a5323a 45%,#e6c2b4 100%);
    --meat2:linear-gradient(160deg,#8e2a2f 0%,#c1484b 55%,#d9a08f 100%);
    --people:linear-gradient(135deg,#d7c3ad 0%,#b08f76 50%,#efe6dc 100%);
    --shop:linear-gradient(135deg,#5b5450 0%,#9a8e84 55%,#d6cfc6 100%);
    --sausage:linear-gradient(135deg,#b86a4a 0%,#d89a6b 55%,#f1dcc6 100%);
  }
  *{box-sizing:border-box;margin:0;padding:0}
  html,body{width:1200px;height:3316px;overflow:hidden}
  body{background:var(--page);font-family:"Source Sans 3",Arial,sans-serif;color:var(--ink);position:relative}

  .ph{display:block}
  .ph.meat{background:var(--meat)}
  .ph.meat2{background:var(--meat2)}
  .ph.people{background:var(--people)}
  .ph.shop{background:var(--shop)}
  .ph.sausage{background:var(--sausage)}
  .ph.portrait{background:linear-gradient(180deg,#cfc4b8 0%,#9f8e80 100%)}

  /* Title slide */
  .title-slide{position:relative;overflow:hidden;background:var(--red);color:var(--white)}
  .title-slide .ts-photo{position:absolute;top:0;right:0;width:62%;height:100%}
  .title-slide .ts-fade{position:absolute;inset:0;background:linear-gradient(90deg,var(--red) 38%,rgba(156,29,47,.55) 70%,rgba(156,29,47,.35) 100%)}
  .title-slide.dark{background:#2b2626}
  .title-slide.dark .ts-fade{background:linear-gradient(90deg,#2b2626 38%,rgba(43,38,38,.55) 75%,rgba(43,38,38,.3))}
  .title-slide.light{background:#f3f0ee;color:var(--red)}
  .title-slide.light .ts-fade{background:linear-gradient(90deg,#f3f0ee 38%,rgba(243,240,238,.5) 75%,rgba(243,240,238,.2))}
  .title-slide.brown{background:var(--brown)}
  .ts-brand{position:absolute;font-weight:700;letter-spacing:.12em}
  .ts-title{position:absolute;font-weight:700;line-height:1.05}
  .ts-sub{position:absolute;opacity:.9}
  .ts-btn{position:absolute;border:1px solid currentColor;border-radius:2px}
  .ts-foot{position:absolute;left:0;right:0;bottom:0;background:var(--white);color:var(--muted);text-align:center}

  .hero{position:absolute;left:100px;top:90px;width:1000px;height:563px;box-shadow:0 8px 30px rgba(0,0,0,.3)}
  .hero .ts-brand{left:56px;top:50px;font-size:38px}
  .hero .ts-title{left:56px;top:190px;font-size:64px}
  .hero .ts-sub{left:56px;top:345px;font-size:24px}
  .hero .ts-btn{left:56px;top:405px;font-size:16px;padding:10px 26px}
  .hero .ts-foot{height:40px;line-height:40px;font-size:14px}

  .deck{position:absolute;left:48px;top:780px;display:grid;grid-template-columns:repeat(3,352px);gap:26px 24px}
  .slide{width:352px;height:198px;position:relative;overflow:hidden;background:var(--white)}
  .slide .ts-brand{left:18px;top:16px;font-size:13px}
  .slide .ts-title{left:18px;top:62px;font-size:22px}
  .slide .ts-sub{left:18px;top:115px;font-size:8px}
  .slide .ts-btn{left:18px;top:134px;font-size:6px;padding:3px 9px}
  .slide .ts-foot{height:14px;line-height:14px;font-size:5px}

  .hd{position:absolute;left:16px;top:14px;font-size:12px;font-weight:700;color:var(--red);line-height:1.1}
  .hd.big{font-size:15px}
  .txt{position:absolute;font-size:6.5px;line-height:1.45;color:#666}
  .slide.brown{background:var(--brown);color:var(--white)}
  .slide.brown .hd{color:var(--white)}
  .slide.brown .txt{color:#eee}
  .abs{position:absolute}
  .cap{font-size:6px;color:var(--ink);text-align:center;margin-top:3px;font-weight:600}
  .row{position:absolute;display:flex;gap:6px}
  .grid{position:absolute;display:grid;gap:4px}
  .band{position:absolute;left:0;right:0;background:var(--red);color:var(--white);font-weight:700;text-align:center}
  .round{border-radius:50%}
</style>
</head>
<body>

<section class="title-slide hero">
  <div class="ph people ts-photo" role="img" aria-label="Familie beim gemeinsamen Essen am Tisch"></div>
  <div class="ts-fade"></div>
  <div class="ts-brand">HOFMARK</div>
  <h1 class="ts-title">Präsentationstitel<br>kommt hierher</h1>
  <p class="ts-sub">Untertitel der Präsentation geht hier</p>
  <div class="ts-btn">Datum, Ort 2024</div>
  <div class="ts-foot">© 2024 Hofmark GmbH · Dorfstraße 12 · 4600 Wels · www.hofmark-fleisch.at</div>
</section>

<main class="deck">
  <!-- row 1 -->
  <section class="title-slide slide"><div class="ph people ts-photo" role="img" aria-label="Familie am Esstisch"></div><div class="ts-fade"></div><div class="ts-brand">HOFMARK</div><h2 class="ts-title">Präsentationstitel<br>kommt hierher</h2><p class="ts-sub">Untertitel der Präsentation geht hier</p><div class="ts-btn">Datum, Ort</div><div class="ts-foot">© 2024 Hofmark GmbH · Dorfstraße 12 · 4600 Wels</div></section>
  <section class="title-slide slide light"><div class="ph people ts-photo" role="img" aria-label="Gäste beim Essen"></div><div class="ts-fade"></div><div class="ts-brand">HOFMARK</div><h2 class="ts-title">Präsentationstitel<br>kommt hierher</h2><p class="ts-sub">Untertitel der Präsentation geht hier</p><div class="ts-btn">Datum, Ort</div><div class="ts-foot">© 2024 Hofmark GmbH · Dorfstraße 12 · 4600 Wels</div></section>
  <section class="title-slide slide"><div class="ph meat ts-photo" role="img" aria-label="Rohe Fleischstücke"></div><div class="ts-fade"></div><div class="ts-brand">HOFMARK</div><h2 class="ts-title">Präsentationstitel<br>kommt hierher</h2><p class="ts-sub">Untertitel der Präsentation geht hier</p><div class="ts-btn">Datum, Ort</div><div class="ts-foot">© 2024 Hofmark GmbH · Dorfstraße 12 · 4600 Wels</div></section>
  <!-- row 2 -->
  <section class="title-slide slide dark"><div class="ph people ts-photo" role="img" aria-label="Gemeinsames Essen"></div><div class="ts-fade"></div><div class="ts-brand">HOFMARK</div><h2 class="ts-title">Präsentationstitel<br>kommt hierher</h2><p class="ts-sub">Untertitel der Präsentation geht hier</p><div class="ts-btn">Datum, Ort</div><div class="ts-foot">© 2024 Hofmark GmbH · Dorfstraße 12 · 4600 Wels</div></section>
  <section class="title-slide slide"><div class="ph meat2 ts-photo" role="img" aria-label="Fleisch auf Schneidbrett"></div><div class="ts-fade"></div><div class="ts-brand">HOFMARK</div><h2 class="ts-title">Präsentationstitel<br>kommt hierher</h2><p class="ts-sub">Untertitel der Präsentation geht hier</p><div class="ts-btn">Datum, Ort</div><div class="ts-foot">© 2024 Hofmark GmbH · Dorfstraße 12 · 4600 Wels</div></section>
  <section class="title-slide slide"><div class="ph meat ts-photo" role="img" aria-label="Steaks in der Theke"></div><div class="ts-fade"></div><div class="ts-brand">HOFMARK</div><h2 class="ts-title">Präsentationstitel<br>kommt hierher</h2><p class="ts-sub">Untertitel der Präsentation geht hier</p><div class="ts-btn">Datum, Ort</div><div class="ts-foot">© 2024 Hofmark GmbH · Dorfstraße 12 · 4600 Wels</div></section>
  <!-- row 3 -->
  <section class="title-slide slide"><div class="ph meat2 ts-photo" role="img" aria-label="Rohes Fleisch"></div><div class="ts-fade"></div><div class="ts-brand">HOFMARK</div><h2 class="ts-title">Präsentationstitel<br>kommt hierher</h2><p class="ts-sub">Untertitel der Präsentation geht hier</p><div class="ts-btn">Datum, Ort</div><div class="ts-foot">© 2024 Hofmark GmbH · Dorfstraße 12 · 4600 Wels</div></section>
  <section class="title-slide slide"><div class="ts-brand">HOFMARK</div><h2 class="ts-title">Präsentationstitel<br>kommt hierher</h2><p class="ts-sub">Untertitel der Präsentation geht hier</p><div class="ts-btn">Datum, Ort</div><div class="ts-foot">© 2024 Hofmark GmbH · Dorfstraße 12 · 4600 Wels</div></section>
  <section class="title-slide slide brown"><div class="ts-brand">HOFMARK</div><h2 class="ts-title">Präsentationstitel<br>kommt hierher</h2><p class="ts-sub">Untertitel der Präsentation geht hier</p><div class="ts-btn">Datum, Ort</div><div class="ts-foot">© 2024 Hofmark GmbH · Dorfstraße 12 · 4600 Wels</div></section>

  <!-- row 4 -->
  <section class="slide">
    <h3 class="hd">Überschrift kommt hierher</h3>
    <div class="row" style="left:16px;top:60px">
      <div><div class="ph sausage" style="width:74px;height:50px" role="img" aria-label="Würstel"></div><p class="cap">WÜRSTEL</p></div>
      <div><div class="ph sausage" style="width:74px;height:50px" role="img" aria-label="Leberkäse"></div><p class="cap">LEBERKÄSE</p></div>
      <div><div class="ph meat2" style="width:74px;height:50px" role="img" aria-label="Speck"></div><p class="cap">SPECK</p></div>
      <div><div class="ph meat" style="width:74px;height:50px" role="img" aria-label="Frischfleisch"></div><p class="cap">FRISCHFLEISCH</p></div>
    </div>
  </section>
  <section class="slide">
    <div class="ph meat abs" style="left:0;top:0;width:176px;height:198px" role="img" aria-label="Fleischstücke auf Brett"></div>
    <h3 class="hd" style="left:192px;top:40px">Hergestellt<br>mit Handarbeit</h3>
    <p class="txt" style="left:192px;top:80px;width:140px">Alle Produkte entstehen bei uns im Haus, von Hand und nach alten Rezepten aus der Region.</p>
  </section>
  <section class="slide">
    <h3 class="hd" style="top:24px">Frische- und<br>Wursttheke</h3>
    <p class="txt" style="left:16px;top:62px;width:150px">Täglich frisch aus eigener Herstellung. Kurze Wege vom Bauernhof bis zu unserer Theke.</p>
    <div class="ph shop abs" style="left:196px;top:0;width:156px;height:198px" role="img" aria-label="Verkaufstheke im Geschäft"></div>
  </section>

  <!-- row 5 -->
  <section class="slide">
    <div class="ph people abs" style="left:0;top:0;width:150px;height:198px" role="img" aria-label="Mitarbeiter bei der Arbeit"></div>
    <h3 class="hd" style="left:166px;top:40px">Mitarbeiterangabe<br>hier</h3>
    <p class="txt" style="left:166px;top:80px;width:170px">Kurzer Text über das Team und die tägliche Arbeit im Betrieb.</p>
  </section>
  <section class="slide brown">
    <h3 class="hd" style="top:70px">Betriebsleitung<br>Fleischhauerei Hofmark</h3>
    <div class="ph portrait abs" style="left:210px;top:34px;width:110px;height:120px" role="img" aria-label="Porträt der Betriebsleitung"></div>
    <p class="txt" style="left:210px;top:160px">Vorname Nachname</p>
  </section>
  <section class="slide brown">
    <h3 class="hd">Das Team der Fleischhauerei Hofmark</h3>
    <div class="row" style="left:16px;top:60px">
      <div><div class="ph portrait" style="width:58px;height:66px" role="img" aria-label="Teammitglied"></div><p class="cap" style="color:#fff">Name</p></div>
      <div><div class="ph portrait" style="width:58px;height:66px" role="img" aria-label="Teammitglied"></div><p class="cap" style="color:#fff">Name</p></div>
      <div><div class="ph portrait" style="width:58px;height:66px" role="img" aria-label="Teammitglied"></div><p class="cap" style="color:#fff">Name</p></div>
      <div><div class="ph portrait" style="width:58px;height:66px" role="img" aria-label="Teammitglied"></div><p class="cap" style="color:#fff">Name</p></div>
      <div><div class="ph portrait" style="width:58px;height:66px" role="img" aria-label="Teammitglied"></div><p class="cap" style="color:#fff">Name</p></div>
    </div>
  </section>

  <!-- row 6 -->
  <section class="slide brown">
    <h3 class="hd">Das Team der Fleischhauerei</h3>
    <div class="row" style="left:16px;top:50px;gap:5px">
      <div class="ph portrait" style="width:49px;height:56px" role="img" aria-label="Teammitglied"></div>
      <div class="ph portrait" style="width:49px;height:56px" role="img" aria-label="Teammitglied"></div>
      <div class="ph portrait" style="width:49px;height:56px" role="img" aria-label="Teammitglied"></div>
      <div class="ph portrait" style="width:49px;height:56px" role="img" aria-label="Teammitglied"></div>
      <div class="ph portrait" style="width:49px;height:56px" role="img" aria-label="Teammitglied"></div>
      <div class="ph portrait" style="width:49px;height:56px" role="img" aria-label="Teammitglied"></div>
    </div>
    <div class="row" style="left:16px;top:116px;gap:5px">
      <div class="ph portrait" style="width:49px;height:56px" role="img" aria-label="Teammitglied"></div>
      <div class="ph portrait" style="width:49px;height:56px" role="img" aria-label="Teammitglied"></div>
      <div class="ph portrait" style="width:49px;height:56px" role="img" aria-label="Teammitglied"></div>
      <div class="ph portrait" style="width:49px;height:56px" role="img" aria-label="Teammitglied"></div>
      <div class="ph portrait" style="width:49px;height:56px" role="img" aria-label="Teammitglied"></div>
      <div class="ph portrait" style="width:49px;height:56px" role="img" aria-label="Teammitglied"></div>
    </div>
  </section>
  <section class="slide">
    <h3 class="hd">Der Fotoshoot kommt hierher</h3>
    <div class="grid" style="left:16px;top:44px;grid-template-columns:repeat(4,77px);grid-auto-rows:66px">
      <div class="ph meat" role="img" aria-label="Fleisch"></div><div class="ph sausage" role="img" aria-label="Wurstwaren"></div><div class="ph people" role="img" aria-label="Arbeit in der Werkstatt"></div><div class="ph meat2" role="img" aria-label="Steak"></div>
      <div class="ph shop" role="img" aria-label="Geschäft"></div><div class="ph meat" role="img" aria-label="Fleisch"></div><div class="ph sausage" role="img" aria-label="Würstel"></div><div class="ph people" role="img" aria-label="Verkauf"></div>
    </div>
  </section>
  <section class="slide">
    <h3 class="hd" style="top:30px">Der Fotoshoot<br>kommt hierher</h3>
    <p class="txt" style="left:16px;top:70px;width:110px">Platz für einen kurzen Text zu den Bildern dieser Seite.</p>
    <div class="grid" style="left:140px;top:16px;grid-template-columns:repeat(2,96px);grid-auto-rows:80px">
      <div class="ph meat" role="img" aria-label="Fleisch"></div><div class="ph people" role="img" aria-label="Arbeit mit Fleisch"></div>
      <div class="ph sausage" role="img" aria-label="Wurst"></div><div class="ph meat2" role="img" aria-label="Steak"></div>
    </div>
  </section>

  <!-- row 7 -->
  <section class="slide">
    <h3 class="hd">Der Fotoshoot kommt hierher</h3>
    <div class="row" style="left:16px;top:44px">
      <div class="ph sausage" style="width:104px;height:70px" role="img" aria-label="Würstel"></div>
      <div class="ph meat" style="width:104px;height:70px" role="img" aria-label="Fleisch"></div>
      <div class="ph meat2" style="width:104px;height:70px" role="img" aria-label="Speck"></div>
    </div>
    <div class="row" style="left:16px;top:120px">
      <div class="ph meat2" style="width:104px;height:62px" role="img" aria-label="Fleisch"></div>
      <div class="ph sausage" style="width:104px;height:62px" role="img" aria-label="Wurst"></div>
      <div class="ph meat" style="width:104px;height:62px" role="img" aria-label="Steak"></div>
    </div>
  </section>
  <section class="slide">
    <h3 class="hd">Der Fotoshoot kommt hierher</h3>
    <div class="ph meat abs" style="left:16px;top:44px;width:156px;height:138px" role="img" aria-label="Fleisch groß"></div>
    <div class="grid" style="left:180px;top:44px;grid-template-columns:repeat(2,76px);grid-auto-rows:67px">
      <div class="ph meat2" role="img" aria-label="Fleisch"></div><div class="ph meat" role="img" aria-label="Fleisch"></div>
      <div class="ph sausage" role="img" aria-label="Wurst"></div><div class="ph meat2" role="img" aria-label="Steak"></div>
    </div>
  </section>
  <section class="slide">
    <div class="grid" style="left:0;top:0;grid-template-columns:repeat(2,100px);grid-auto-rows:97px">
      <div class="ph meat" role="img" aria-label="Fleisch"></div><div class="ph people" role="img" aria-label="Arbeit"></div>
      <div class="ph sausage" role="img" aria-label="Wurst"></div><div class="ph meat2" role="img" aria-label="Steak"></div>
    </div>
    <h3 class="hd" style="left:218px;top:40px">Der Fotoshoot<br>hier eingefügt</h3>
    <p class="txt" style="left:218px;top:80px;width:120px">Kurzer Text zu den Bildern dieser Seite.</p>
  </section>

  <!-- row 8 -->
  <section class="slide">
    <h3 class="hd" style="top:40px">Überschrift<br>kommt hierher</h3>
    <p class="txt" style="left:16px;top:80px;width:100px">Kurzer Beschreibungstext zum Thema dieser Folie.</p>
    <div class="grid" style="left:124px;top:16px;grid-template-columns:repeat(3,70px);grid-auto-rows:80px">
      <div class="ph meat" role="img" aria-label="Fleisch"></div><div class="ph meat2" role="img" aria-label="Fleisch"></div><div class="ph meat" role="img" aria-label="Fleisch"></div>
      <div class="ph meat2" role="img" aria-label="Fleisch"></div><div class="ph meat" role="img" aria-label="Fleisch"></div><div class="ph meat2" role="img" aria-label="Fleisch"></div>
    </div>
  </section>
  <section class="slide">
    <h3 class="hd" style="top:40px">Überschrift<br>kommt hierher</h3>
    <p class="txt" style="left:16px;top:80px;width:100px">Kurzer Beschreibungstext zum Thema dieser Folie.</p>
    <div class="grid" style="left:124px;top:16px;grid-template-columns:repeat(3,70px);grid-auto-rows:80px">
      <div class="ph meat2" role="img" aria-label="Fleisch"></div><div class="ph meat" role="img" aria-label="Fleisch"></div><div class="ph sausage" role="img" aria-label="Wurst"></div>
      <div class="ph meat" role="img" aria-label="Fleisch"></div><div class="ph sausage" role="img" aria-label="Wurst"></div><div class="ph meat2" role="img" aria-label="Fleisch"></div>
    </div>
  </section>
  <section class="slide">
    <div class="grid" style="left:16px;top:16px;grid-template-columns:repeat(4,77px);grid-auto-rows:80px">
      <div class="ph meat" role="img" aria-label="Fleisch"></div><div class="ph meat2" role="img" aria-label="Fleisch"></div><div class="ph meat" role="img" aria-label="Fleisch"></div><div class="ph meat2" role="img" aria-label="Fleisch"></div>
      <div class="ph meat2" role="img" aria-label="Fleisch"></div><div class="ph meat" role="img" aria-label="Fleisch"></div><div class="ph meat2" role="img" aria-label="Fleisch"></div><div class="ph meat" role="img" aria-label="Fleisch"></div>
    </div>
  </section>

  <!-- row 9 -->
  <section class="slide">
    <h3 class="hd">Überschrift kommt hierher</h3>
    <div class="ph people abs" style="left:16px;top:44px;width:200px;height:138px" role="img" aria-label="Familie am Tisch"></div>
    <div class="grid" style="left:224px;top:44px;grid-template-columns:112px;grid-auto-rows:67px">
      <div class="ph meat" role="img" aria-label="Fleisch"></div><div class="ph sausage" role="img" aria-label="Wurst"></div>
    </div>
  </section>
  <section class="slide">
    <h3 class="hd">Überschrift kommt hierher</h3>
    <div class="ph people abs" style="left:16px;top:44px;width:200px;height:138px" role="img" aria-label="Gäste am Tisch"></div>
    <div class="grid" style="left:224px;top:44px;grid-template-columns:112px;grid-auto-rows:67px">
      <div class="ph meat2" role="img" aria-label="Fleisch"></div><div class="ph meat" role="img" aria-label="Steak"></div>
    </div>
  </section>
  <section class="slide">
    <h3 class="hd">Überschrift kommt hierher</h3>
    <div class="row" style="left:16px;top:44px">
      <div class="ph meat" style="width:104px;height:138px" role="img" aria-label="Fleisch"></div>
      <div class="ph people" style="width:104px;height:138px" role="img" aria-label="Familie"></div>
      <div class="ph meat2" style="width:104px;height:138px" role="img" aria-label="Fleisch"></div>
    </div>
  </section>

  <!-- row 10 -->
  <section class="slide">
    <h3 class="hd">Überschrift kommt hierher</h3>
    <div class="row" style="left:16px;top:44px">
      <div class="ph people" style="width:158px;height:138px" role="img" aria-label="Gemeinsames Essen"></div>
      <div class="ph meat" style="width:158px;height:138px" role="img" aria-label="Fleisch"></div>
    </div>
  </section>
  <section class="slide">
    <h3 class="hd">Überschrift kommt hierher</h3>
    <div class="grid" style="left:16px;top:44px;grid-template-columns:repeat(3,104px);grid-auto-rows:67px">
      <div class="ph people" role="img" aria-label="Essen"></div><div class="ph meat" role="img" aria-label="Fleisch"></div><div class="ph meat2" role="img" aria-label="Fleisch"></div>
      <div class="ph meat2" role="img" aria-label="Fleisch"></div><div class="ph people" role="img" aria-label="Essen"></div><div class="ph meat" role="img" aria-label="Fleisch"></div>
    </div>
  </section>
  <section class="slide">
    <h3 class="hd">Überschrift kommt hierher</h3>
    <div class="ph people abs" style="left:16px;top:44px;width:150px;height:138px" role="img" aria-label="Familie am Tisch"></div>
    <div class="grid" style="left:172px;top:44px;grid-template-columns:repeat(2,80px);grid-auto-rows:67px">
      <div class="ph meat" role="img" aria-label="Fleisch"></div><div class="ph meat2" role="img" aria-label="Fleisch"></div>
      <div class="ph meat2" role="img" aria-label="Fleisch"></div><div class="ph meat" role="img" aria-label="Fleisch"></div>
    </div>
  </section>

  <!-- row 11 -->
  <section class="slide">
    <div class="ph meat abs" style="left:0;top:0;width:352px;height:198px" role="img" aria-label="Steaks und Fleischstücke"></div>
    <div class="band" style="bottom:0;height:24px;line-height:24px;font-size:10px">WEIL REGIONALES BESSER SCHMECKT</div>
  </section>
  <section class="slide brown">
    <div class="ts-brand abs" style="left:18px;top:16px;font-size:13px;font-weight:700;letter-spacing:.12em">HOFMARK</div>
    <h3 class="hd" style="left:200px;top:50px">Kontakt</h3>
    <p class="txt" style="left:200px;top:72px;width:140px">Fleischhauerei Hofmark GmbH<br>Dorfstraße 12<br>4600 Wels<br>Tel. +43 7242 000 000<br>info@hofmark-fleisch.at<br>www.hofmark-fleisch.at</p>
  </section>
</main>

</body>
</html>
```